Special Educational Conference Poster

Looking for a poster that I can use electronically more than anything - to post on Chatterbook \ social media. Should be bold, eye catching, and within our brand colors.

3rd Annual Young Learners Beyond Limits Summit
Featuring Dr. Martin Ellery
Lighting the Way: Growing Courage, Drive, and Grit in Every Young Learner Who Thinks Differently

Friday, May 10, 2019, 9am - 3pm

The Linden Grove Academy at Fenwick opens our campus to teachers, parents, and practitioners from the Delaware Valley to learn together on how to support the extraordinary students in our lives. The conference runs from 9am - 3pm and lunch is included. This event is free and open to the public, but registration is required.

Link to registration: https://www.lindengroveacad.org/admissions/admissions-visit-and-events

```html
<!DOCTYPE html>
<html lang="en">
<head>
<meta charset="utf-8">
<title>Young Learners Beyond Limits Summit</title>
<link rel="stylesheet" href="https://fonts.googleapis.com/css2?family=Arvo:wght@700&family=Jost:wght@500;600;700&family=Tinos:wght@400;700&display=swap">
<style>
  :root {
    --navy: #1f3348;
    --gold: #e2bf3a;
    --gold-soft: #d9b845;
    --white: #ffffff;
    --orange: #f5a13a;
    --orange-deep: #d9822b;
    --photo-tone: #c9c4bd;
  }
  * { margin: 0; padding: 0; box-sizing: border-box; }
  html, body {
    width: 1200px;
    height: 959px;
    overflow: hidden;
    background: var(--navy);
  }
  .poster {
    position: relative;
    width: 1200px;
    height: 959px;
    background: var(--navy);
    color: var(--white);
    overflow: hidden;
  }
  .summit-title {
    position: absolute;
    left: 58px;
    top: 34px;
    font-family: "Arvo", "Rockwell", serif;
    font-weight: 700;
    color: var(--gold);
  }
  .summit-title .edition {
    display: block;
    font-size: 47px;
    line-height: 52px;
  }
  .summit-title .name {
    display: block;
    font-size: 35px;
    line-height: 44px;
  }
  .speaker-photo {
    position: absolute;
    left: 60px;
    top: 211px;
    width: 251px;
    height: 228px;
    background: linear-gradient(160deg, #f4f4f4 0%, var(--photo-tone) 55%, #3b4a63 100%);
  }
  .speaker-line {
    position: absolute;
    left: 60px;
    top: 452px;
    font-family: "Tinos", "Times New Roman", serif;
    font-size: 25px;
    color: var(--white);
  }
  .speaker-line strong { font-weight: 700; }
  .talk {
    position: absolute;
    left: 60px;
    top: 498px;
    font-family: "Jost", "Futura", sans-serif;
  }
  .talk-title {
    font-size: 44px;
    line-height: 52px;
    font-weight: 700;
    color: var(--gold);
  }
  .talk-subtitle {
    font-size: 27px;
    line-height: 36px;
    font-weight: 600;
    color: var(--white);
  }
  .talk-date {
    margin-top: 4px;
    font-size: 28px;
    line-height: 36px;
    font-weight: 600;
    color: var(--gold);
  }
  .details {
    position: absolute;
    left: 60px;
    top: 678px;
    width: 1100px;
    font-family: "Jost", "Futura", sans-serif;
    font-weight: 500;
    font-size: 24.5px;
    line-height: 38px;
    color: var(--white);
  }
  .registration {
    position: absolute;
    left: 60px;
    top: 870px;
    font-family: "Jost", "Futura", sans-serif;
    font-weight: 500;
    font-size: 24.5px;
    line-height: 38px;
    color: var(--gold-soft);
  }
  .mind-artwork {
    position: absolute;
    left: 610px;
    top: 18px;
    width: 560px;
    height: 630px;
    border-radius: 46% 46% 40% 40%;
    background: radial-gradient(ellipse at 55% 30%, rgba(245,161,58,0.55) 0%, rgba(217,130,43,0.28) 38%, rgba(31,51,72,0) 70%);
  }
</style>
</head>
<body>
  <main class="poster">
    <h1 class="summit-title">
      <span class="edition">3rd Annual</span>
      <span class="name">Young Learners Beyond</span>
      <span class="name">Limits Summit</span>
    </h1>

    <div class="speaker-photo" role="img" aria-label="Portrait photograph of the featured speaker, Dr. Martin Ellery"></div>
    <p class="speaker-line">Featuring <strong>Dr. Martin Ellery</strong></p>

    <section class="talk">
      <h2 class="talk-title">Lighting the Way:</h2>
      <p class="talk-subtitle">Growing Courage, Drive, and Grit in Every Young<br>Learner Who Thinks Differently</p>
      <p class="talk-date">Friday, May 10, 2019, 9am - 3pm</p>
    </section>

    <p class="details">The Linden Grove Academy at Fenwick opens our campus to teachers, parents, and practitioners from the Delaware Valley to learn together on how to support the extraordinary students in our lives. The conference runs from 9am - 3pm and lunch is included. This event is free and open to the public, but registration is required.</p>

    <p class="registration">Link to registration:<br>https://www.lindengroveacad.org/admissions/admissions-visit-and-events</p>

    <div class="mind-artwork" role="img" aria-label="Illustration of a glowing orange outline of a head in profile with a gear-filled brain, its line ending in an electrical plug"></div>
  </main>
</body>
</html>
```